We need an eye catching logo design and Business Card that portrays our business, which is the cleaning and protecting of stainless steel with an organic non chemical product. This can be separate to the company name or can incorporate it. Maybe even just the company name itself. Company Name is Gleamwise Gleamwise.
Ideal for products exposed to weather elements, ie: balustrading, enclosures, BBQs, we also supply the product so you can do it yourself (DIY).
In addition we would want to include on this card:
1. My Name (Paul Dremmick)
2. Mobile No. (TBA Later)
3. Email address (TBA Later)
4. Web address (TBA Later)
Updates

Please note that we also need suggestions on a logo, as this we do not have this either.

Please note we have update our brief to be more specific.

Thank You.

Paul

Reason: Awaiting for a couple of revised submissions from feedback given.

Target Market(s)

Purchasing officers and government people.

Industry/Entity Type

Steel

Colors

Designer to choose colors to be used in the design.

Requirements
Must have
• 1. Name (Paul Dremmick)
2. Mobile No. (TBA Later)
Should not have
• Should not be to busy looking

```html
<!DOCTYPE html>
<html lang="en">
<head>
<meta charset="utf-8">
<title>Paul Dremmick – Business Card</title>
<link rel="stylesheet" href="https://fonts.googleapis.com/css2?family=Italiana&family=Questrial&display=swap">
<style>
  :root {
    --page: #ffffff;
    --top-light: #96a0ae;
    --top-dark: #78818f;
    --bottom-light: #60646d;
    --bottom-dark: #46494f;
    --rule: #4e5560;
    --rule-glow: #a9b2c4;
    --steel-dark: #7a767c;
    --steel-mid: #bdbcc0;
    --steel-light: #f2f2f4;
    --steel-grey: #a4a4a7;
    --ink: #3a3a3d;
    --on-band: #ffffff;
  }
  * { box-sizing: border-box; margin: 0; padding: 0; }
  html, body {
    width: 1200px; height: 1000px; overflow: hidden;
    background: var(--page);
  }
  .card {
    position: absolute; left: 46px; top: 158px;
    width: 1110px; height: 684px;
  }
  .band-top {
    position: absolute; left: 0; top: 0; width: 100%; height: 194px;
    background: linear-gradient(to bottom, var(--top-light), var(--top-dark));
  }
  .rule {
    position: absolute; left: 0; width: 100%; height: 4px;
    background: linear-gradient(to bottom, var(--rule) 0 50%, var(--rule-glow) 50% 100%);
  }
  .rule-upper { top: 194px; }
  .rule-lower { top: 499px; }
  .plate {
    position: absolute; left: 0; top: 198px; width: 100%; height: 301px;
    background: linear-gradient(160deg,
      var(--steel-dark) 0%, var(--steel-mid) 22%, var(--steel-light) 34%,
      var(--steel-mid) 48%, #c9c9cc 58%, var(--steel-grey) 68%,
      #bfbfc2 80%, var(--steel-light) 88%, var(--steel-grey) 100%);
  }
  .band-bottom {
    position: absolute; left: 0; top: 503px; width: 100%; height: 181px;
    background: linear-gradient(to bottom, var(--bottom-light), var(--bottom-dark));
  }
  .contact {
    position: absolute; display: flex; align-items: center;
    font-family: "Questrial", "Century Gothic", sans-serif;
    color: var(--on-band); font-size: 33px; letter-spacing: 0.5px;
  }
  .contact svg { flex: none; }
  .contact-phone { left: 166px; top: 112px; gap: 48px; }
  .contact-fax { left: 648px; top: 112px; gap: 40px; }
  .contact-email { left: 377px; top: 568px; gap: 38px; }
  .name {
    position: absolute; left: 0; top: 272px; width: 100%;
    text-align: center;
    font-family: "Italiana", "Didot", serif;
    font-size: 110px; line-height: 1; color: var(--ink);
    letter-spacing: 1px;
  }
  .website {
    position: absolute; left: 0; top: 453px; width: 100%;
    text-align: center;
    font-family: "Questrial", "Century Gothic", sans-serif;
    font-size: 23px; color: var(--ink); letter-spacing: 0.5px;
  }
</style>
</head>
<body>
  <div class="card">
    <div class="band-top"></div>
    <div class="rule rule-upper"></div>
    <div class="plate"></div>
    <div class="rule rule-lower"></div>
    <div class="band-bottom"></div>

    <div class="contact contact-phone">
      <svg width="54" height="54" viewBox="0 0 54 54" aria-hidden="true">
        <circle cx="27" cy="27" r="24" fill="none" stroke="#fff" stroke-width="3.5"/>
        <path d="M19 15 l5 -2 l4 8 l-3 3 c1 4 3 7 6 9 l3 -3 l7 5 l-2 5 c-10 2 -21 -12 -20 -25z" fill="#fff"/>
      </svg>
      <span>1800 42 7316</span>
    </div>

    <div class="contact contact-fax">
      <svg width="54" height="54" viewBox="0 0 54 54" aria-hidden="true">
        <circle cx="27" cy="27" r="24" fill="none" stroke="#fff" stroke-width="3.5"/>
        <rect x="19" y="11" width="16" height="16" fill="none" stroke="#fff" stroke-width="2"/>
        <path d="M22 16 h10 M22 20 h10 M22 24 h7" stroke="#fff" stroke-width="1.5"/>
        <rect x="13" y="27" width="28" height="13" rx="2" fill="#fff"/>
        <rect x="19" y="31" width="16" height="5" fill="#7e8796"/>
      </svg>
      <span>1800 42 7316</span>
    </div>

    <h1 class="name">Paul Dremmick</h1>
    <p class="website">www.yourwebsitehere.com</p>

    <div class="contact contact-email">
      <svg width="53" height="38" viewBox="0 0 53 38" aria-hidden="true">
        <rect x="1.5" y="1.5" width="50" height="35" fill="none" stroke="#fff" stroke-width="3"/>
        <path d="M1.5 1.5 L26.5 22 L51.5 1.5 M1.5 36.5 L20 17 M51.5 36.5 L33 17" fill="none" stroke="#fff" stroke-width="3"/>
      </svg>
      <span>paul@gleammail.com</span>
    </div>
  </div>
</body>
</html>
```